Psychotherapist's business card

I need a business card design for a psychotherapist. I expect business card to have "light" design. By this I mean that it can somehow translate easiness, serenity. Maybe pastel colours can help you here. I have attached some pictures from Greece. Perhaps they can inspire you to combine colours and to achieve that "light" design.
Updates

Pls, don't use any free samples you may find on business card generators. It looks too simple, uncreative and waste of time! READ size and colour requirements! I don't want to see any shapes like rings, triangles etc.

Contact Information for Business Card

Size: 65mmX60mm

Name - Мирослав Гречихин

Психолог
+7(916)482-39-07
grechikhin.com

I suppose that thin font can look good but it's up to you

Requirements
Must have
• size requirements
Nice to have
• pastel colours
• thin font
Should not have
• black and dark colours
• lines, free design samples used from other web-sites

```html
<!DOCTYPE html>
<html lang="ru">
<head>
<meta charset="utf-8">
<title>Мирослав Гречихин — Психолог</title>
<link rel="stylesheet" href="https://fonts.googleapis.com/css2?family=Exo+2:wght@200;300&display=swap">
<style>
  :root {
    --page-bg: #ecedec;
    --card-base: #dfeae6;
    --card-light: #f4f8f6;
    --mint-soft: #c9dcd5;
    --ink: #7d8583;
    --ink-soft: #8e9694;
  }
  * { margin: 0; padding: 0; box-sizing: border-box; }
  html, body {
    width: 1200px;
    height: 900px;
    overflow: hidden;
    background: var(--page-bg);
  }
  .stage {
    width: 1200px;
    height: 900px;
    display: flex;
    align-items: center;
    justify-content: center;
  }
  /* 65 × 60 mm at 10 px per mm */
  .business-card {
    position: relative;
    width: 650px;
    height: 600px;
    background: var(--card-base);
    overflow: hidden;
    box-shadow: 0 6px 22px rgba(90, 110, 105, 0.18);
    font-family: "Exo 2", sans-serif;
    color: var(--ink);
  }
  .card-backdrop {
    position: absolute;
    inset: 0;
    width: 100%;
    height: 100%;
  }
  .holder-name {
    position: absolute;
    left: 0;
    right: 0;
    top: 180px;
    text-align: center;
    font-weight: 200;
    font-size: 52px;
    letter-spacing: 0.5px;
    white-space: nowrap;
  }
  .holder-role {
    position: absolute;
    left: 330px;
    top: 252px;
    font-weight: 200;
    font-size: 30px;
    color: var(--ink-soft);
  }
  .contacts {
    position: absolute;
    left: 130px;
    top: 360px;
    font-style: normal;
    font-weight: 300;
    font-size: 34px;
    line-height: 50px;
    color: var(--ink-soft);
  }
  .contacts a { color: inherit; text-decoration: none; display: block; }
  .contacts .contact-web { margin-left: -6px; }
</style>
</head>
<body>
<main class="stage">
  <section class="business-card">
    <svg class="card-backdrop" viewBox="0 0 650 600" role="img" aria-label="Мягкий мятный фон с расходящимися от центра светлыми лучами и акварельными мазками" preserveAspectRatio="none">
      <defs>
        <radialGradient id="glow" cx="0.5" cy="0.5" r="0.62">
          <stop offset="0" stop-color="var(--card-light)"/>
          <stop offset="0.55" stop-color="#e8f0ed"/>
          <stop offset="1" stop-color="var(--mint-soft)"/>
        </radialGradient>
      </defs>
      <rect width="650" height="600" fill="url(#glow)"/>
    </svg>

    <h1 class="holder-name">Мирослав Гречихин</h1>
    <p class="holder-role">Психолог</p>

    <address class="contacts">
      <a class="contact-phone" href="tel:+79164823907">+7(916)482-39-07</a>
      <a class="contact-web" href="https://grechikhin.com">grechikhin.com</a>
    </address>
  </section>
</main>
</body>
</html>
```